TRAVIM 2026 Flyer for Conference

TRAVIM needs a design for a 1-page flyer that we will hand out at an upcoming event & then later post online as a pdf. There are 3 elements which need to be on the flyer:

1) A logo. This should be prominent on the design (e.g., in the middle). The flyer should use the colors that are in that logo (e.g., for accents, design elements, and/or text; not all of these have to be used):
Dark blue: #185577
Med blue: #327C9A
Teal: #4EB1C2
Light Teal: #9EDBE6

2) The conference theme -- Oceans of Knowledge: Diving into Information Literacy -- should be at the flyer's top.

3) Finally, these six tracks should be listed below the theme and the logo (it's font size should be at least a couple sizes smaller than the size used for the theme):
- Pearls of Pedagogy: Teaching Techniques that Work
- The Depth Gauge: Measuring Instructional Impact
- Techtonic Shifts: Innovation and Educational Technology
- Captain's Log: Navigating Leadership in Library Instruction
- Swimming Together: Collaborating with Others
- The Bermuda Triangle: Exploring (Seemingly) Eternal Challenges

Font styles to use
Sans Serif

Colors
0094D4
00A9DD
6FCCEA
C7EBF8
E9F6FB

Requirements
Must have
• The 3 elements listed in the description: 1) the logo, 2) the text of the theme and 3) the text for the tracks.

```html
<!DOCTYPE html>
<html lang="en">
<head>
<meta charset="utf-8">
<title>TRAVIM 2026 Conference Flyer</title>
<link href="https://fonts.googleapis.com/css2?family=Roboto+Condensed:wght@400;500&family=Montserrat:wght@500;600&display=swap" rel="stylesheet">
<style>
  :root {
    --dark-blue: #185577;
    --med-blue: #327C9A;
    --teal: #4EB1C2;
    --light-teal: #9EDBE6;
    --panel-grey: #EFEFF1;
    --paper: #FFFFFF;
    --photo-sky: #B98A6A;
    --photo-city: #3C4A5E;
  }
  * { box-sizing: border-box; margin: 0; padding: 0; }
  html, body { width: 986px; height: 1200px; overflow: hidden; background: var(--paper); }
  .flyer { position: relative; width: 986px; height: 1200px; background: var(--paper); font-family: "Roboto Condensed", sans-serif; }
  .side-panel { position: absolute; left: 0; top: 0; width: 365px; height: 1200px; background: var(--panel-grey); }

  .brand { position: absolute; left: 60px; top: 150px; display: flex; align-items: center; gap: 14px; }
  .brand-dot { width: 40px; height: 40px; border-radius: 50%; background: var(--teal); }
  .brand-name { font-family: "Roboto Condensed", sans-serif; font-weight: 500; font-size: 48px; color: var(--dark-blue); letter-spacing: 1px; }

  .theme { position: absolute; left: 406px; top: 100px; }
  .theme-title { font-size: 60px; font-weight: 400; color: var(--dark-blue); line-height: 1; }
  .theme-subtitle { margin-left: 6px; margin-top: 10px; font-size: 52px; font-weight: 400; color: var(--med-blue); line-height: 1.12; width: 520px; }

  .rule-white { position: absolute; left: 120px; top: 369px; width: 245px; height: 10px; background: var(--paper); }
  .rule-teal { position: absolute; left: 643px; top: 873px; width: 245px; height: 10px; background: var(--light-teal); }

  .tracks { position: absolute; left: 106px; top: 411px; width: 782px; height: 436px; background: var(--dark-blue); }
  .tracks-heading { position: absolute; left: 16px; top: 42px; font-size: 68px; font-weight: 400; color: var(--teal); line-height: 1; }
  .track { position: absolute; border-left: 3px solid var(--light-teal); padding-left: 20px; width: 330px; font-family: "Montserrat", sans-serif; color: var(--paper); }
  .track-name { font-size: 20px; font-weight: 600; line-height: 1.3; }
  .track-desc { font-size: 15.5px; font-weight: 500; line-height: 1.3; margin-top: 4px; }
  .col-left { left: 28px; }
  .col-right { left: 456px; width: 310px; }
  .row-1 { top: 144px; }
  .row-2 { top: 237px; }
  .row-3 { top: 339px; }

  .date { position: absolute; left: 56px; top: 938px; color: var(--dark-blue); }
  .date-year { font-size: 128px; font-weight: 500; line-height: 1; }
  .date-range { font-size: 44px; font-weight: 400; line-height: 1; margin-top: 2px; }

  .city { position: absolute; left: 365px; top: 941px; width: 455px; height: 149px; background: linear-gradient(180deg, var(--photo-sky) 0%, #7A6A6E 35%, var(--photo-city) 60%, #2E3A4C 100%); }
  .city-name { position: absolute; left: 19px; top: 48px; font-size: 54px; font-weight: 500; color: var(--paper); line-height: 1; }
</style>
</head>
<body>
<main class="flyer">
  <div class="side-panel"></div>

  <div class="brand">
    <span class="brand-dot"></span>
    <span class="brand-name">TRAVIM 2026</span>
  </div>

  <header class="theme">
    <h1 class="theme-title">Oceans of Knowledge</h1>
    <p class="theme-subtitle">Diving Into Information Literacy</p>
  </header>

  <div class="rule-white"></div>

  <section class="tracks">
    <h2 class="tracks-heading">The Six Tracks</h2>
    <div class="track col-left row-1"><div class="track-name">Pearls of Pedagogy</div><div class="track-desc">Teaching Techniques that Work</div></div>
    <div class="track col-right row-1"><div class="track-name">The Depth Gauge</div><div class="track-desc">Measuring Instructional Impact</div></div>
    <div class="track col-left row-2"><div class="track-name">Techtonic Shifts</div><div class="track-desc">Innovation &amp; Educational Technology</div></div>
    <div class="track col-right row-2"><div class="track-name">Captain's Log</div><div class="track-desc">Navigating Leadership in Library Instruction</div></div>
    <div class="track col-left row-3"><div class="track-name">Swimming Together</div><div class="track-desc">Collaborating with Others</div></div>
    <div class="track col-right row-3"><div class="track-name">The Bermuda Triangle</div><div class="track-desc">Exploring (Seemingly) Eternal Challenges</div></div>
  </section>

  <div class="rule-teal"></div>

  <div class="date">
    <div class="date-year">2026</div>
    <div class="date-range">MAY 7 - MAY 9</div>
  </div>

  <div class="city" role="img" aria-label="Aerial photo of the host city skyline at sunset">
    <span class="city-name">NORFOLK, VA</span>
  </div>
</main>
</body>
</html>
```